copper meadow

It is a small business that is looking to sell medical supplies and services. later down the line it will branch off to help solve other world problems, i.e. global warming and raw material shortages.
but we will start with hospital equipment and supplies.

Target Market(s)

all medical facilities

Coding

Coded - Design and coding required

Number of Pages Required

1 page

```html
<!DOCTYPE html>
<html lang="en">
<head>
<meta charset="utf-8">
<title>Copper Meadow — Hospital Equipment and Supplies</title>
<link href="https://fonts.googleapis.com/css2?family=Montserrat:ital,wght@0,500;0,600;0,700;0,800;1,700;1,800&family=Lato:ital,wght@0,400;0,700;1,400&display=swap" rel="stylesheet">
<style>
:root{
  --cyan:#3bb4d8;
  --red:#e8405a;
  --ink:#1e1e24;
  --muted:#555a63;
  --panel:#f2f3f5;
  --navy:#1c3a8c;
  --orange:#f2a23a;
  --white:#fff;
}
*{box-sizing:border-box;margin:0;padding:0}
html,body{width:1200px;height:4528px;overflow:hidden}
body{position:relative;background:var(--white);font-family:'Lato',sans-serif;color:var(--ink)}
.abs{position:absolute}
.head{font-family:'Montserrat',sans-serif}
.center{text-align:center;left:0;width:1200px}

/* top bar */
.topbar{left:0;top:0;width:1200px;height:38px;background:var(--cyan);color:#fff;font-size:12px;line-height:38px;text-align:center}
.logo{font-family:'Montserrat',sans-serif;font-weight:800;font-size:23px;letter-spacing:.3px;color:var(--ink);text-transform:uppercase}
.search{left:323px;top:53px;width:366px;height:52px;border:1.5px solid #333;border-radius:26px;font-size:13px;line-height:49px;padding-left:24px;color:#333}
.search .go{position:absolute;right:6px;top:5px;width:40px;height:40px;border-radius:50%;background:var(--cyan);display:flex;align-items:center;justify-content:center}
.icon-ring{top:57px;width:44px;height:44px;border-radius:50%;border:1.5px solid var(--cyan);display:flex;align-items:center;justify-content:center}
.icon-ring span{width:30px;height:30px;border-radius:50%;background:var(--cyan);display:flex;align-items:center;justify-content:center}
.callbox{left:887px;top:38px;width:313px;height:85px;background:var(--panel)}
.callbox .ring{position:absolute;left:12px;top:20px;width:44px;height:44px;border-radius:50%;border:1.5px solid var(--cyan);display:flex;align-items:center;justify-content:center}
.callbox .label{position:absolute;left:67px;top:22px;font-size:11px;color:var(--red)}
.callbox .num{position:absolute;left:67px;top:36px;font-family:'Montserrat',sans-serif;font-weight:700;font-size:19px;color:var(--ink)}

/* nav */
.nav{left:0;top:123px;width:1200px;height:53px;background:var(--cyan)}
.nav a{position:absolute;top:0;line-height:53px;color:#fff;font-family:'Montserrat',sans-serif;font-weight:600;font-size:12px;text-decoration:none;transform:translateX(-50%)}

/* hero */
.hero{left:0;top:176px;width:1200px;height:601px;background:linear-gradient(180deg,#4a5f80 0%,#3b5478 45%,#33476a 100%)}
.hero-title{top:350px;font-family:'Montserrat',sans-serif;font-weight:800;font-size:58px;line-height:62px;color:#fff;letter-spacing:.5px}
.hero-copy{top:480px;left:250px;width:700px;text-align:center;font-size:12.5px;line-height:25px;color:#fff}
.btn{display:flex;align-items:center;justify-content:center;border-radius:26px;color:#fff;font-family:'Montserrat',sans-serif;font-weight:700;font-size:14px;letter-spacing:.3px}
.arrow{width:46px;height:46px;border-radius:50%;display:flex;align-items:center;justify-content:center}
.arrow.light{border:1.5px solid #fff}
.arrow.dark{border:1.5px solid #222}

.redline{left:0;width:1200px;height:3px;background:var(--red)}

/* promo cards */
.promo{top:738px;width:453px;height:244px;overflow:hidden;box-shadow:0 6px 14px rgba(0,0,0,.15)}
.promo .blob{position:absolute;width:300px;height:300px;border-radius:50%}
.promo .badge{position:absolute;left:23px;top:37px;height:30px;padding:0 8px;line-height:30px;color:#fff;font-size:13px}
.promo .title{position:absolute;left:23px;top:86px;font-family:'Montserrat',sans-serif;font-weight:600;font-size:19px;line-height:27px}
.promo .btn{position:absolute;left:23px;top:158px;width:175px;height:49px}
.promo .prod{position:absolute}

/* headings */
.sec-title{font-family:'Montserrat',sans-serif;font-weight:700;font-size:32px;color:var(--ink)}
.bar{width:62px;height:3px;background:var(--cyan);left:569px}

.about-copy{left:622px;top:1186px;width:466px;font-size:11.6px;line-height:24px;color:#333;text-align:justify}

/* stats */
.stats{left:0;top:1678px;width:1200px;height:246px;background:linear-gradient(180deg,#1c3f93 0%,#2148a0 50%,#173679 100%)}
.stat{top:1767px;width:240px;text-align:center;transform:translateX(-50%)}
.stat b{display:block;font-family:'Montserrat',sans-serif;font-weight:800;font-size:32px;color:var(--cyan);line-height:40px}
.stat span{display:block;font-size:15.5px;color:var(--red);line-height:20px}

/* tabs & products */
.tabs{font-family:'Montserrat',sans-serif;font-weight:600;font-size:14px}
.tabs .on{color:var(--cyan)}
.card{width:225px;text-align:center}
.card .pic{width:225px;height:224px;background:var(--panel);display:flex;align-items:center;justify-content:center}
.card .name{margin-top:18px;font-family:'Montserrat',sans-serif;font-weight:600;font-size:16px;color:var(--ink)}
.card .stars{margin-top:3px;color:var(--orange);font-size:12px;letter-spacing:1px}
.card .price{margin-top:3px;color:var(--red);font-size:15px}

/* feedback */
.feedback{left:0;top:2490px;width:1200px;height:476px;background:linear-gradient(180deg,#2a8fd6 0%,#2c7ed0 50%,#1e63bd 100%)}
.quote{top:2634px;width:457px;height:221px;background:#fff;border-radius:12px}
.quote p{position:absolute;left:30px;top:22px;width:405px;font-style:italic;font-size:11.6px;line-height:24px;color:#333}
.quote .avatar{position:absolute;left:27px;top:173px;width:96px;height:96px;border-radius:50%;background:linear-gradient(180deg,#c9d3dc,#7f8d9a);border:3px solid #fff}
.quote .who{position:absolute;left:153px;top:174px;font-family:'Montserrat',sans-serif;font-weight:700;font-size:15px;color:var(--red)}
.quote .stars{position:absolute;right:40px;top:174px;color:var(--orange);font-size:12px;letter-spacing:1px}

/* contact */
.contact-bg{left:0;top:3561px;width:1200px;height:572px;background:#f4f5f7}
.contact-blue{left:177px;top:3644px;width:338px;height:283px;background:var(--cyan)}
.contact-blue .kick{position:absolute;right:97px;top:70px;font-family:'Montserrat',sans-serif;font-weight:700;font-size:14px;color:#fff}
.contact-blue .big{position:absolute;right:97px;top:104px;text-align:right;font-family:'Montserrat',sans-serif;font-weight:800;font-style:italic;font-size:31px;line-height:40px;color:#fff}
.frame{border:3px solid var(--red)}
.form{left:455px;top:3679px;width:532px;height:362px;background:#fff;box-shadow:0 6px 18px rgba(0,0,0,.08)}
.form h2{position:absolute;left:37px;top:36px;font-family:'Montserrat',sans-serif;font-weight:700;font-size:23px;color:var(--ink)}
.field{position:absolute;width:215px;border-bottom:1px solid #cfd3d8;height:44px}
.field label{display:block;font-family:'Montserrat',sans-serif;font-weight:600;font-size:12px;color:var(--ink)}
.field span{display:block;margin-top:12px;font-size:10px;color:#777}
.dots{left:155px;top:3883px;width:167px;height:70px;background-image:radial-gradient(circle,#333 1.4px,transparent 1.6px);background-size:9px 9px}

/* footer */
.footer{left:0;top:4140px;width:1200px;height:388px;background:#000;color:#fff}
.ftitle{font-family:'Montserrat',sans-serif;font-weight:700;font-size:14px;color:var(--red)}
.flinks{font-size:13px;line-height:28px}
.flinks li{list-style:none;padding-left:26px;position:relative}
.flinks li:before{content:"»";position:absolute;left:4px;color:var(--cyan)}
.social{top:4313px;width:30px;height:30px;border-radius:50%;background:var(--cyan)}
.fcontact{font-size:13px;line-height:24px}
.fcontact .dot{position:absolute;left:0;width:28px;height:28px;border-radius:50%;background:var(--cyan);display:flex;align-items:center;justify-content:center}
.pay{top:4464px;width:22px;height:15px;background:#fff;border-radius:2px}
.fbottom{top:4464px;font-size:11.5px}
</style>
</head>
<body>

<div class="abs topbar">Lorem ipsum dolor sit amet, consectetur adipiscing elit, sed do eiusmod</div>

<!-- header -->
<div class="abs logo" style="left:100px;top:64px">Copper Meadow</div>
<div class="abs search">search your product
  <span class="go"><svg width="16" height="16" viewBox="0 0 16 16"><circle cx="7" cy="7" r="4.5" fill="none" stroke="#fff" stroke-width="2"/><line x1="10.5" y1="10.5" x2="14" y2="14" stroke="#fff" stroke-width="2"/></svg></span>
</div>
<div class="abs icon-ring" style="left:712px"><span><svg width="14" height="14" viewBox="0 0 14 14"><path d="M7 12 L2 7 A2.8 2.8 0 0 1 7 3.5 A2.8 2.8 0 0 1 12 7 Z" fill="#fff"/></svg></span></div>
<div class="abs icon-ring" style="left:767px"><span><svg width="14" height="14" viewBox="0 0 14 14"><circle cx="7" cy="4.5" r="2.8" fill="#fff"/><path d="M2 13 Q7 6 12 13Z" fill="#fff"/></svg></span></div>
<div class="abs icon-ring" style="left:823px"><span><svg width="14" height="14" viewBox="0 0 14 14"><path d="M1 2H3L5 9H11L12.5 4H4" fill="none" stroke="#fff" stroke-width="1.6"/><circle cx="5.5" cy="11.5" r="1.2" fill="#fff"/><circle cx="10.5" cy="11.5" r="1.2" fill="#fff"/></svg></span></div>
<div class="abs callbox">
  <div class="ring"><svg width="18" height="18" viewBox="0 0 18 18"><path d="M4 2 L7 2 L8 6 L6 7.5 Q7.5 11 10.5 12 L12 10 L16 11 L16 14 Q15 16 12 15.5 Q5 13 2.5 5 Q2.5 2.5 4 2Z" fill="none" stroke="var(--cyan)" stroke-width="1.5"/></svg></div>
  <div class="label">CALL US TODAY</div>
  <div class="num">+1 555 0142 786</div>
</div>

<nav class="abs nav">
  <a style="left:339px">HOME</a>
  <a style="left:429px">ABOUT</a>
  <a style="left:531px">PRODUCTS</a>
  <a style="left:641px">REVIEWS</a>
  <a style="left:743px">GALLERY</a>
  <a style="left:849px">CONTACT</a>
</nav>

<!-- hero -->
<div class="abs hero" role="img" aria-label="Photo of a modern operating theatre with surgical lamps and scanning equipment"></div>
<h1 class="abs center hero-title">HOSPITAL EQUIPMENT<br>AND SUPPLIES</h1>
<p class="abs hero-copy">Lorem ipsum dolor sit amet, consectetur adipiscing elit, sed do eiusmod tempor incididunt ut labore et dolore magna aliqua. Ut enim ad minim veniam, quis nostrud exercitation</p>
<div class="abs btn" style="left:511px;top:541px;width:176px;height:49px;background:var(--cyan)">GET STARTED</div>
<div class="abs arrow light" style="left:46px;top:451px"><svg width="12" height="14" viewBox="0 0 12 14"><path d="M8 2 L3 7 L8 12" fill="none" stroke="#fff" stroke-width="1.6"/></svg></div>
<div class="abs arrow light" style="left:1105px;top:451px"><svg width="12" height="14" viewBox="0 0 12 14"><path d="M4 2 L9 7 L4 12" fill="none" stroke="#fff" stroke-width="1.6"/></svg></div>

<div class="abs redline" style="top:779px"></div>

<!-- promo cards -->
<div class="abs promo" style="left:132px;background:#f5f3ea">
  <div class="blob" style="left:250px;top:-20px;background:#efedd6"></div>
  <div class="badge" style="background:var(--orange)">NEW ARRIVAL</div>
  <div class="title">Digital Thermometer<br>gun for Covid - 19</div>
  <div class="btn" style="background:var(--red)">SHOP NOW</div>
  <div class="prod" role="img" aria-label="Infrared thermometer gun" style="left:320px;top:25px;width:110px;height:200px;border-radius:40px 40px 20px 20px;background:linear-gradient(160deg,#c5cdd8,#8fa4c2)"></div>
</div>
<div class="abs promo" style="left:613px;background:#3f9ed9">
  <div class="blob" style="left:240px;top:-25px;background:#5fb3e4"></div>
  <div class="badge" style="background:#3f5ee0">NEW ARRIVAL</div>
  <div class="title" style="color:#fff">Face mask &amp;<br>Thermometer Gun</div>
  <div class="btn" style="background:var(--cyan)">SHOP NOW</div>
  <div class="prod" role="img" aria-label="Surgical face masks with a thermometer gun" style="left:265px;top:35px;width:170px;height:170px;border-radius:20px;background:linear-gradient(150deg,#a9d6f1,#e6eef5)"></div>
</div>

<!-- welcome -->
<h2 class="abs center sec-title" style="top:1059px">Welcome To Copper Meadow</h2>
<div class="abs bar" style="top:1110px"></div>

<div class="abs frame" style="left:112px;top:1154px;width:382px;height:343px"></div>
<div class="abs" role="img" aria-label="Photo of a clean hospital operating room" style="left:128px;top:1170px;width:397px;height:353px;background:linear-gradient(160deg,#a7b8c6,#5e7687 60%,#3f5361)"></div>
<div class="abs frame" style="left:372px;top:1337px;width:213px;height:239px"></div>
<div class="abs" role="img" aria-label="Photo of masks, thermometer gun, syringes and pills on blue" style="left:365px;top:1330px;width:213px;height:237px;background:linear-gradient(150deg,#4fa9e0,#88c6ec)"></div>

<p class="abs about-copy">Lorem ipsum dolor sit amet, consectetur adipiscing elit, sed do eiusmod tempor incididunt ut labore et dolore magna aliqua. Ut enim ad minim veniam, quis nostrud exercitation ullamco laboris nisi ut aliquip ex ea commodo consequat. Duis aute irure dolor in reprehenderit in voluptate velit esse cillum dolore eu fugiat nulla pariatur. Excepteur sint occaecat cupidatat non proident, sunt in culpa qui officia deserunt mollit anim id est laborumSed ut perspiciatis unde omnis iste natus error sit voluptatem accusantium doloremque laudantium, totam rem aperiam, eaque ipsa quae ab illo inventore veritatis et quasi architecto beatae vitae dicta sunt explicabo. Nemo enim ipsam voluptatem quia voluptas sit aspernatur aut odit aut fugit, sed quia consequuntur magni dolores eos qui ratione voluptatem sequi nesciunt. Neque porro quisquam est, qui dolorem ipsum quia dolor sit amet, consectetur, adipisci velit, sed quia non numquam eius modi tempora incidunt.</p>
<div class="abs btn" style="left:622px;top:1490px;width:174px;height:47px;background:var(--cyan)">LEARN MORE</div>

<!-- stats -->
<div class="abs redline" style="top:1669px"></div>
<div class="abs stats" role="img" aria-label="Blue-tinted photo of hospital equipment"></div>
<div class="abs redline" style="top:1930px"></div>
<div class="abs stat" style="left:244px"><b>930k+</b><span>Nostrud exercitation</span></div>
<div class="abs stat" style="left:483px"><b>930k+</b><span>Nostrud exercitation</span></div>
<div class="abs stat" style="left:724px"><b>930k+</b><span>Nostrud exercitation</span></div>
<div class="abs stat" style="left:965px"><b>930k+</b><span>Nostrud exercitation</span></div>

<!-- featured products -->
<h2 class="abs center sec-title" style="top:1993px">Our Featured Product</h2>
<div class="abs bar" style="top:2045px"></div>
<div class="abs center tabs" style="top:2078px">EQUIPMENT &nbsp;&nbsp;&nbsp;&nbsp;| &nbsp;&nbsp;&nbsp;&nbsp;<span class="on">SUPPLIES</span></div>

<div class="abs arrow dark" style="left:46px;top:2233px"><svg width="12" height="14" viewBox="0 0 12 14"><path d="M8 2 L3 7 L8 12" fill="none" stroke="#222" stroke-width="1.6"/></svg></div>
<div class="abs arrow dark" style="left:1105px;top:2233px"><svg width="12" height="14" viewBox="0 0 12 14"><path d="M4 2 L9 7 L4 12" fill="none" stroke="#222" stroke-width="1.6"/></svg></div>

<div class="abs card" style="left:132px;top:2121px"><div class="pic"><div role="img" aria-label="Stethoscope with red heart-shaped tubing" style="width:150px;height:90px;border-radius:45px;background:linear-gradient(90deg,#3a3a3a,#d9313e)"></div></div><div class="name">Digital Stethoscope</div><div class="stars">★★★★★</div><div class="price">$250</div></div>
<div class="abs card" style="left:369px;top:2121px"><div class="pic"><div role="img" aria-label="Blood pressure monitor with red hearts" style="width:150px;height:130px;border-radius:50%;background:linear-gradient(150deg,#d9313e,#2a2a2a)"></div></div><div class="name">Sphygmomanometer</div><div class="stars">★★★★★</div><div class="price">$250</div></div>
<div class="abs card" style="left:606px;top:2121px"><div class="pic"><div role="img" aria-label="White and blue infrared thermometer" style="width:170px;height:90px;border-radius:30px;background:linear-gradient(90deg,#e8edf2,#5bbbe6)"></div></div><div class="name">Thermometer</div><div class="stars">★★★★★</div><div class="price">$250</div></div>
<div class="abs card" style="left:843px;top:2121px"><div class="pic"><div role="img" aria-label="Blue hand sanitizer pump bottle" style="width:60px;height:160px;border-radius:14px;background:linear-gradient(180deg,#9fd3ef,#2f8fcf)"></div></div><div class="name">Hand Sanitizer</div><div class="stars">★★★★★</div><div class="price">$250</div></div>

<!-- feedback -->
<div class="abs redline" style="top:2481px"></div>
<div class="abs feedback" role="img" aria-label="Blue-tinted photo of a laboratory scientist at work"></div>
<div class="abs redline" style="top:2971px"></div>
<h2 class="abs center head" style="top:2553px;font-weight:700;font-size:33px;color:#fff">Customer Feedback</h2>
<div class="abs" style="left:86px;top:2734px"><svg width="24" height="26" viewBox="0 0 24 26"><path d="M16 3 L6 13 L16 23" fill="none" stroke="#fff" stroke-width="2.4"/></svg></div>
<div class="abs" style="left:1090px;top:2734px"><svg width="24" height="26" viewBox="0 0 24 26"><path d="M8 3 L18 13 L8 23" fill="none" stroke="#fff" stroke-width="2.4"/></svg></div>

<div class="abs quote" style="left:132px">
  <p>Sed ut perspiciatis unde omnis iste natus error sit voluptatem accusa ntium doloremque laudantium, totam rem aperiam, eaque ipsa quae ab illo inventore veritatis et quasi architecto beatae vitae dicta sunt expl icabo. Nemo enim ipsam voluptatem quia voluptas sit aspernatur aut odit aut fugit, sed quia consequuntur magni dolores eos qui ratione voluptatem sequi nesciunt.</p>
  <div class="avatar" role="img" aria-label="Customer portrait"></div>
  <div class="who">DANIEL REYES</div>
  <div class="stars">★★★★★</div>
</div>
<div class="abs quote" style="left:610px">
  <p>Sed ut perspiciatis unde omnis iste natus error sit voluptatem accusa ntium doloremque laudantium, totam rem aperiam, eaque ipsa quae ab illo inventore veritatis et quasi architecto beatae vitae dicta sunt expl icabo. Nemo enim ipsam voluptatem quia voluptas sit aspernatur aut odit aut fugit, sed quia consequuntur magni dolores eos qui ratione voluptatem sequi nesciunt.</p>
  <div class="avatar" role="img" aria-label="Customer portrait"></div>
  <div class="who">DANIEL REYES</div>
  <div class="stars">★★★★★</div>
</div>

<!-- self protection kit -->
<h2 class="abs center sec-title" style="top:3050px">Self Protection Kit</h2>
<div class="abs bar" style="top:3102px"></div>
<div class="abs center tabs" style="top:3136px">EQUIPMENT &nbsp;&nbsp;&nbsp;&nbsp;| &nbsp;&nbsp;&nbsp;&nbsp;<span class="on">SUPPLIES</span></div>

<div class="abs arrow dark" style="left:46px;top:3291px"><svg width="12" height="14" viewBox="0 0 12 14"><path d="M8 2 L3 7 L8 12" fill="none" stroke="#222" stroke-width="1.6"/></svg></div>
<div class="abs arrow dark" style="left:1105px;top:3291px"><svg width="12" height="14" viewBox="0 0 12 14"><path d="M4 2 L9 7 L4 12" fill="none" stroke="#222" stroke-width="1.6"/></svg></div>

<div class="abs card" style="left:132px;top:3178px"><div class="pic"><div role="img" aria-label="Black stethoscope" style="width:170px;height:100px;border-radius:50px;background:linear-gradient(90deg,#444,#9aa0a6)"></div></div><div class="name">Digital Stethoscope</div><div class="stars">★★★★★</div><div class="price">$250</div></div>
<div class="abs card" style="left:369px;top:3178px"><div class="pic"><div role="img" aria-label="Digital blood pressure monitor with cuff" style="width:170px;height:160px;border-radius:20px;background:linear-gradient(150deg,#9b92c9,#2d2d35)"></div></div><div class="name">Sphygmomanometer</div><div class="stars">★★★★★</div><div class="price">$250</div></div>
<div class="abs card" style="left:606px;top:3178px"><div class="pic"><div role="img" aria-label="Digital stick thermometer" style="width:190px;height:26px;border-radius:13px;transform:rotate(-30deg);background:linear-gradient(90deg,#e3e7ec,#2f62c9)"></div></div><div class="name">Thermometer</div><div class="stars">★★★★★</div><div class="price">$250</div></div>
<div class="abs card" style="left:843px;top:3178px"><div class="pic"><div role="img" aria-label="Clear hand sanitizer pump bottle" style="width:64px;height:170px;border-radius:14px;background:linear-gradient(180deg,#f4f6f8,#d3dbe2)"></div></div><div class="name">Hand Sanitizer</div><div class="stars">★★★★★</div><div class="price">$250</div></div>

<!-- contact -->
<div class="abs contact-bg"></div>
<div class="abs frame" style="left:750px;top:3644px;width:271px;height:374px"></div>
<div class="abs dots"></div>
<div class="abs contact-blue">
  <div class="kick">CONTACT US</div>
  <div class="big">LET’S GO<br>GOOD<br>TOGETHER</div>
</div>
<div class="abs form">
  <h2>SEND US A MESSAGE</h2>
  <div class="field" style="left:37px;top:86px"><label>YOUR NAME</label><span>Jane Park</span></div>
  <div class="field" style="left:274px;top:86px;width:216px"><label>COMPANY</label><span>jane@coppermeadow.example</span></div>
  <div class="field" style="left:37px;top:162px"><label>EMAIL ADDRESS</label><span>jane@coppermeadow.example</span></div>
  <div class="field" style="left:274px;top:162px;width:216px"><label>PHONE</label><span>1 555 014 278</span></div>
  <div class="field" style="left:37px;top:242px;width:410px;height:73px"><label>MESSAGE</label><span>Hi , do you have a moment to talk about Us</span></div>
  <div class="abs" style="left:447px;top:277px;width:48px;height:48px;border-radius:50%;background:var(--cyan);display:flex;align-items:center;justify-content:center"><svg width="20" height="20" viewBox="0 0 20 20"><path d="M2 10 L18 3 L13 18 L10 12 Z" fill="#fff"/></svg></div>
</div>
<div class="abs redline" style="top:4133px"></div>

<!-- footer -->
<footer class="abs footer"></footer>
<div class="abs logo" style="left:132px;top:4268px;color:#fff">Copper Meadow</div>
<div class="abs social" style="left:131px"></div>
<div class="abs social" style="left:182px"></div>
<div class="abs social" style="left:234px"></div>
<div class="abs social" style="left:285px"></div>

<div class="abs ftitle" style="left:378px;top:4205px">QUICK LINKS</div>
<ul class="abs flinks" style="left:378px;top:4234px">
  <li>Home</li><li>About</li><li>Products</li><li>Reviews</li><li>Gallery</li><li>Contact</li>
</ul>

<div class="abs ftitle" style="left:571px;top:4205px">CONTACT US</div>
<div class="abs fcontact" style="left:575px;top:4238px;width:220px;height:60px">
  <span class="dot" style="top:4px"><svg width="12" height="14" viewBox="0 0 12 14"><path d="M6 13 Q1 7 1 5 A5 5 0 0 1 11 5 Q11 7 6 13Z" fill="#fff"/><circle cx="6" cy="5" r="1.8" fill="var(--cyan)"/></svg></span>
  <div style="padding-left:42px">123 Lorem ipsum dolor sit et, consectetur adip.</div>
</div>
<div class="abs fcontact" style="left:575px;top:4306px;width:220px;height:30px">
  <span class="dot" style="top:-2px"><svg width="14" height="14" viewBox="0 0 18 18"><path d="M4 2 L7 2 L8 6 L6 7.5 Q7.5 11 10.5 12 L12 10 L16 11 L16 14 Q15 16 12 15.5 Q5 13 2.5 5 Q2.5 2.5 4 2Z" fill="#fff"/></svg></span>
  <div style="padding-left:42px">+1 555 0142 786</div>
</div>
<div class="abs fcontact" style="left:575px;top:4360px;width:240px;height:30px">
  <span class="dot" style="top:-2px"><svg width="14" height="12" viewBox="0 0 14 12"><rect x="1" y="1" width="12" height="10" fill="#fff"/><path d="M1 1 L7 6 L13 1" fill="none" stroke="var(--cyan)" stroke-width="1.2"/></svg></span>
  <div style="padding-left:42px">hello@coppermeadow.example</div>
</div>

<div class="abs ftitle" style="left:838px;top:4205px">SIGN UP FOR OUR NEWSLETTER</div>
<p class="abs" style="left:843px;top:4232px;width:240px;font-size:12.5px;line-height:25px;color:#fff">Lorem ipsum dolor sit amet, consectetur adipiscing elit, sed do.</p>
<div class="abs" style="left:843px;top:4300px;width:201px;height:36px;background:#fff;font-size:10px;line-height:36px;padding-left:12px;color:#777">Enter The Email</div>
<div class="abs" style="left:1044px;top:4300px;width:52px;height:36px;background:var(--cyan);display:flex;align-items:center;justify-content:center"><svg width="16" height="16" viewBox="0 0 20 20"><path d="M2 10 L18 3 L13 18 L10 12 Z" fill="#fff"/></svg></div>
<div class="abs" style="left:1028px;top:4370px;width:48px;height:48px;border-radius:50%;background:var(--red);display:flex;align-items:center;justify-content:center"><svg width="22" height="20" viewBox="0 0 22 20"><path d="M11 2 C5 2 2 5.5 2 9 C2 11 3 12.8 5 14 L4 18 L8.5 15.6 C9.3 15.8 10.1 16 11 16 C17 16 20 12.5 20 9 C20 5.5 17 2 11 2Z" fill="#fff"/><circle cx="7.5" cy="9" r="1.2" fill="var(--red)"/><circle cx="11" cy="9" r="1.2" fill="var(--red)"/><circle cx="14.5" cy="9" r="1.2" fill="var(--red)"/></svg></div>

<div class="abs fbottom" style="left:132px;color:#fff">© copyrights 2022 Copper Meadow &nbsp;|&nbsp; All Rights Reserved</div>
<div class="abs pay" style="left:580px"></div>
<div class="abs pay" style="left:607px"></div>
<div class="abs pay" style="left:634px"></div>
<div class="abs pay" style="left:661px"></div>
<div class="abs fbottom" style="left:891px;color:#fff">Privacy policy &nbsp;|&nbsp; Terms of Service</div>

</body>
</html>
```